Brava Nest (Smart Home, Installation, Repair Industry) (Contest)

Looking for a website design for my company
Services we offer:
Phone Repair
TV Mounting
Security Camera Installation
Networking / Wi-Fi
Smart Home Services
IT Support

Looking for a website similar to trovely.example

Few tabs
About Us
Contact Us
Areas Served
Pricing and Services

```html
<!DOCTYPE html>
<html lang="en">
<head>
<meta charset="utf-8">
<title>Brava Nest – Home Maintenance Made Simple</title>
<link href="https://fonts.googleapis.com/css2?family=Catamaran:wght@400;500;600;700&family=Montserrat:wght@400;500;600&display=swap" rel="stylesheet">
<style>
:root{
  --orange:#f7931e;
  --orange-dark:#ee7f12;
  --ink:#222222;
  --muted:#555555;
  --panel:#3a3a3a;
  --footer:#1c1c1c;
  --light:#f6f6f6;
  --white:#ffffff;
  --line:#d6d6d6;
}
*{box-sizing:border-box;margin:0;padding:0}
html,body{width:1200px;height:4461px;overflow:hidden}
body{position:relative;font-family:"Montserrat",sans-serif;color:var(--ink);background:var(--white)}
.abs{position:absolute}
.head{font-family:"Catamaran",sans-serif}
.orange{color:var(--orange)}
.btn{position:absolute;display:flex;align-items:center;justify-content:center;background:var(--orange);color:var(--white);font-family:"Catamaran",sans-serif;font-size:18px}

/* hero */
.hero{position:absolute;left:0;top:0;width:1200px;height:687px;background:linear-gradient(90deg,#f4f4f4 0%,#e8e8e6 40%,#cfcac4 70%,#b9b3ab 100%)}
.brand{position:absolute;left:111px;top:22px;font-family:"Catamaran",sans-serif;font-weight:700;font-size:50px;line-height:60px;color:var(--orange)}
.nav{position:absolute;top:42px;right:112px;display:flex;gap:20px;font-size:15px;font-family:"Catamaran",sans-serif;font-weight:500}
.nav a{color:var(--ink);text-decoration:none}
.nav a.active{color:var(--orange);text-decoration:underline}
.hero h1{position:absolute;left:111px;top:206px;font-family:"Catamaran",sans-serif;font-weight:700;font-size:40px;line-height:46px;color:var(--ink)}
.hero p{position:absolute;left:111px;top:318px;font-family:"Catamaran",sans-serif;font-size:21px;line-height:30px;color:var(--ink)}

/* services */
.services-band{position:absolute;left:0;top:687px;width:1200px;height:149px;background:var(--orange)}
.services-band h2{position:absolute;width:100%;top:66px;text-align:center;font-family:"Catamaran",sans-serif;font-weight:400;font-size:36px;color:var(--white)}
.services-band h2 b{font-weight:700}
.service-row{position:absolute;left:5px;top:836px;display:flex;gap:4px}
.service{width:195px;height:198px;background:var(--white);display:flex;flex-direction:column;align-items:center;padding-top:40px;text-align:center;font-family:"Catamaran",sans-serif;font-size:20px;line-height:28px}
.service svg{width:52px;height:52px;margin-bottom:20px}
.service.accent{color:var(--orange)}

/* targets */
.targets{position:absolute;left:0;top:1034px;width:1200px;height:606px;background:linear-gradient(90deg,#8a7766 0%,#4a4038 45%,#2a2522 100%)}
.targets h2{position:absolute;left:629px;top:84px;font-family:"Catamaran",sans-serif;font-weight:400;font-size:38px;color:var(--white)}
.targets h2 b{color:var(--orange);font-weight:700}
.target{position:absolute;left:630px;display:flex;align-items:center;gap:26px;color:var(--white)}
.target .dot{width:90px;height:90px;border-radius:50%;border:4px solid var(--white);display:flex;align-items:center;justify-content:center;background:var(--orange)}
.target .dot.grey{background:#8e8e8e}
.target h3{font-family:"Catamaran",sans-serif;font-weight:400;font-size:28px;line-height:34px}
.target p{font-size:16px;margin-top:6px}

/* technicians */
.tech-title{position:absolute;left:0;width:1200px;text-align:center;font-family:"Catamaran",sans-serif}
.tech-card{position:absolute;top:1865px;width:312px;height:229px;border:1px solid var(--line);box-shadow:0 2px 6px rgba(0,0,0,.08);padding:18px 16px}
.tech-card .who{display:flex;gap:12px;align-items:center}
.avatar{width:56px;height:56px;border-radius:50%;background:linear-gradient(135deg,#c9b8a6,#6f6358)}
.tech-card h4{font-family:"Catamaran",sans-serif;font-weight:500;font-size:21px;color:var(--orange);line-height:22px}
.tech-card .role{font-size:13px;color:var(--ink)}
.tech-card .quote{margin-top:22px;font-size:12px;line-height:22px;color:var(--muted);text-align:justify}
.tech-card .foot{margin-top:18px;display:flex;justify-content:space-between;align-items:center;font-size:12px}

/* split */
.split-photo{position:absolute;left:0;top:2194px;width:600px;height:487px;background:linear-gradient(135deg,#5b6f8f 0%,#b9a89a 50%,#e7e2dc 100%)}
.split-panel{position:absolute;left:600px;top:2255px;width:600px;height:485px;background:var(--panel);padding:66px 0 0 50px;color:var(--white)}
.split-panel .mark{font-family:"Catamaran",sans-serif;font-weight:700;font-size:74px;line-height:80px;color:var(--white)}
.split-panel .line1{font-family:"Catamaran",sans-serif;font-size:36px;line-height:40px;margin-top:14px}
.split-panel .line2{font-family:"Catamaran",sans-serif;font-weight:700;font-size:36px;line-height:46px;color:var(--orange)}
.checks{list-style:none;font-size:16px}
.checks li{display:flex;align-items:center;gap:14px;height:31px}
.checks svg{width:18px;height:18px;flex:none}
.split-panel .checks{margin-top:20px}

/* ready */
.ready h2{position:absolute;left:111px;font-family:"Catamaran",sans-serif;font-size:36px}
.mount-photo{position:absolute;left:655px;top:2848px;width:432px;height:330px;background:radial-gradient(circle at 40% 45%,#4a4a4a 0%,#2b2b2b 55%,#ffffff 56%)}

/* news */
.news{position:absolute;left:0;top:3247px;width:1200px;height:756px;background:var(--light)}
.news h2{position:absolute;width:100%;top:70px;text-align:center;font-family:"Catamaran",sans-serif;font-weight:400;font-size:38px}
.news h2 b{color:var(--orange);font-weight:700}
.news .lead{position:absolute;left:111px;width:978px;top:128px;text-align:center;font-size:13.5px;line-height:24px;color:var(--muted)}
.post{position:absolute;top:221px;width:307px;height:442px;background:var(--white);box-shadow:0 2px 8px rgba(0,0,0,.06);text-align:center}
.post .img{height:207px}
.post h3{margin-top:30px;font-size:16px;line-height:24px;font-weight:600;letter-spacing:.5px}
.post p{margin:10px 18px 0;font-size:13px;line-height:23px;color:var(--muted)}
.post .more{display:inline-flex;margin-top:26px;width:100px;height:41px;align-items:center;justify-content:center;border:1px solid #333;font-size:12px}
.post.hot h3{color:var(--orange)}
.post.hot .more{background:var(--orange);border-color:var(--orange);color:var(--white)}

/* footer */
.footer{position:absolute;left:0;top:4003px;width:1200px;height:458px;background:var(--footer);color:var(--white)}
.footer .mark{position:absolute;left:111px;top:160px;font-family:"Catamaran",sans-serif;font-weight:700;font-size:76px;line-height:80px}
.fcol{position:absolute;top:80px}
.fcol h5{font-family:"Catamaran",sans-serif;font-weight:700;font-size:21px;margin-bottom:14px}
.fcol a{display:block;color:var(--white);text-decoration:none;font-size:15px;line-height:27.7px}
.contact-item{display:flex;gap:16px;align-items:flex-start;font-size:15px;line-height:27px;margin-bottom:16px}
.contact-item .ic{width:36px;height:36px;border-radius:50%;background:var(--orange);display:flex;align-items:center;justify-content:center;flex:none}
.footer .rule{position:absolute;left:111px;top:363px;width:978px;height:1px;background:#3c3c3c}
.footer .copy{position:absolute;width:100%;top:397px;text-align:center;font-size:15px}
</style>
</head>
<body>

<!-- Hero -->
<section class="hero" role="img" aria-label="Smiling technicians mounting a flat-screen TV on a living room wall">
</section>
<div class="brand">Brava Nest</div>
<nav class="nav">
  <a class="active" href="#">HOME</a><a href="#">ABOUT US</a><a href="#">AREAS SERVED</a><a href="#">PRICING AND SERVICES</a><a href="#">CONTACT US</a>
</nav>
<div class="hero-copy">
  <h1 class="abs" style="left:111px;top:206px;font-family:'Catamaran',sans-serif;font-weight:700;font-size:40px;line-height:46px">Home Maintenance<br>Made Simple</h1>
  <p class="abs" style="left:111px;top:318px;font-family:'Catamaran',sans-serif;font-size:21px;line-height:30px">The best technicians in your<br>neighborhood.</p>
</div>
<a class="btn" style="left:111px;top:410px;width:125px;height:54px">Contact Us</a>

<!-- Services -->
<section class="services-band"><h2>Services <b>We Offer Are</b></h2></section>
<div class="service-row">
  <div class="service accent"><svg viewBox="0 0 52 52" fill="none" stroke="#f7931e" stroke-width="2"><rect x="12" y="6" width="22" height="38" rx="3"/><rect x="26" y="18" width="16" height="26" rx="2"/><line x1="20" y1="40" x2="26" y2="40"/></svg>Phone Repair</div>
  <div class="service"><svg viewBox="0 0 52 52" fill="none" stroke="#222" stroke-width="2"><rect x="10" y="10" width="28" height="24"/><path d="M38 18h8M38 26h8M46 14v16M4 14v16M4 22h6"/><line x1="16" y1="40" x2="32" y2="40"/></svg>TV Mounting</div>
  <div class="service accent"><svg viewBox="0 0 52 52" fill="none" stroke="#f7931e" stroke-width="2"><path d="M6 12h40v6H6z"/><path d="M12 18c0 12 28 12 28 0"/><circle cx="26" cy="26" r="5"/></svg>Security Camera<br>Installation</div>
  <div class="service"><svg viewBox="0 0 52 52" fill="none" stroke="#222" stroke-width="2"><rect x="6" y="32" width="40" height="12" rx="2"/><line x1="38" y1="32" x2="38" y2="8"/><path d="M14 22a10 10 0 0 1 16 0M18 26a5 5 0 0 1 8 0"/></svg>Networking /<br>Wi-Fi</div>
  <div class="service accent"><svg viewBox="0 0 52 52" fill="none" stroke="#f7931e" stroke-width="2"><path d="M6 26 26 8l20 18"/><path d="M12 22v22h28V22"/><rect x="21" y="30" width="10" height="14"/></svg>Smart Home<br>Services</div>
  <div class="service"><svg viewBox="0 0 52 52" fill="none" stroke="#222" stroke-width="2"><circle cx="26" cy="20" r="10"/><path d="M14 20a12 12 0 0 1 24 0M10 46c2-10 30-10 32 0"/><path d="M38 22v4h-8"/></svg>IT Support</div>
</div>

<!-- Targets -->
<section class="targets" role="img" aria-label="Hand holding a phone with a smart home control app in a modern living room">
  <h2>Our <b>Targets Are</b></h2>
  <div class="target" style="top:172px"><div class="dot"><svg width="40" height="40" viewBox="0 0 52 52" fill="none" stroke="#fff" stroke-width="2.5"><path d="M6 26 26 8l20 18"/><path d="M12 22v22h28V22"/><rect x="21" y="30" width="10" height="14"/></svg></div><div><h3>Smart Home</h3><p>Nemo enim ipsam voluptatem quia voluptas</p></div></div>
  <div class="target" style="top:300px"><div class="dot grey"><svg width="40" height="40" viewBox="0 0 52 52" fill="none" stroke="#fff" stroke-width="2.5"><circle cx="26" cy="20" r="8"/><circle cx="26" cy="20" r="3"/><path d="M6 30l10 14h20l10-14"/></svg></div><div><h3>Installation</h3><p>Nemo enim ipsam voluptatem quia voluptas</p></div></div>
  <div class="target" style="top:428px"><div class="dot"><svg width="40" height="40" viewBox="0 0 52 52" fill="none" stroke="#fff" stroke-width="2.5"><rect x="12" y="6" width="22" height="38" rx="3"/><rect x="26" y="18" width="16" height="26" rx="2"/></svg></div><div><h3>Repair Industry</h3><p>Nemo enim ipsam voluptatem quia voluptas</p></div></div>
</section>

<!-- Technicians -->
<h2 class="tech-title" style="top:1716px;font-weight:400;font-size:36px">Our Top Technicians</h2>
<h2 class="tech-title orange" style="top:1770px;font-weight:700;font-size:37px">Are In Your Neighborhood And Beyond</h2>

<article class="tech-card" style="left:111px">
  <div class="who"><div class="avatar" role="img" aria-label="Technician portrait"></div><div><h4>Marco Delgado</h4><div class="role">BravaNest Technician</div></div></div>
  <p class="quote">Nemo enim ipsam voluptatem quia voluptas sit aspernatur aut odit aut fugit, sed quia consequuntur magni dolores</p>
  <div class="foot"><span>Colette | Los Angeles, CA</span><svg width="84" height="14" viewBox="0 0 84 14" fill="#f7931e"><g id="s"><path d="M7 0l2 5h5l-4 3 2 5-5-3-5 3 2-5-4-3h5z"/></g><use href="#s" x="17"/><use href="#s" x="34"/><use href="#s" x="51"/><use href="#s" x="68"/></svg></div>
</article>
<article class="tech-card" style="left:443px">
  <div class="who"><div class="avatar" role="img" aria-label="Technician portrait"></div><div><h4>Priya Raman</h4><div class="role">BravaNest Technician</div></div></div>
  <p class="quote">Nemo enim ipsam voluptatem quia voluptas sit aspernatur aut odit aut fugit, sed quia consequuntur magni dolores</p>
  <div class="foot"><span>Colette | Los Angeles, CA</span><svg width="84" height="14" viewBox="0 0 84 14" fill="#f7931e"><use href="#s"/><use href="#s" x="17"/><use href="#s" x="34"/><use href="#s" x="51"/><use href="#s" x="68"/></svg></div>
</article>
<article class="tech-card" style="left:774px">
  <div class="who"><div class="avatar" role="img" aria-label="Technician portrait"></div><div><h4>Leon Brandt</h4><div class="role">BravaNest Technician</div></div></div>
  <p class="quote">Nemo enim ipsam voluptatem quia voluptas sit aspernatur aut odit aut fugit, sed quia consequuntur magni dolores</p>
  <div class="foot"><span>Colette | Los Angeles, CA</span><svg width="84" height="14" viewBox="0 0 84 14" fill="#f7931e"><use href="#s"/><use href="#s" x="17"/><use href="#s" x="34"/><use href="#s" x="51"/><use href="#s" x="68"/></svg></div>
</article>

<!-- Split -->
<div class="split-photo" role="img" aria-label="Technician installing a ceiling security camera while a homeowner watches"></div>
<section class="split-panel">
  <div class="mark">Brava Nest</div>
  <div class="line1">A Simple Way</div>
  <div class="line2">To Take Care Of Everything</div>
  <ul class="checks">
    <li><svg viewBox="0 0 18 18" fill="none" stroke="#f7931e" stroke-width="3"><path d="M2 9l5 5 9-11"/></svg>Trusted technicians in your neighborhood</li>
    <li><svg viewBox="0 0 18 18" fill="none" stroke="#f7931e" stroke-width="3"><path d="M2 9l5 5 9-11"/></svg>Guaranteed parts and service + 24/7 support</li>
    <li><svg viewBox="0 0 18 18" fill="none" stroke="#f7931e" stroke-width="3"><path d="M2 9l5 5 9-11"/></svg>Hundreds of repair and install options</li>
  </ul>
</section>

<!-- Ready -->
<section class="ready">
  <h2 style="top:2846px;font-weight:400">Ready To</h2>
  <h2 class="orange" style="top:2898px;font-weight:700">Get Started With BravaNest</h2>
  <ul class="checks abs" style="left:111px;top:2975px;color:var(--ink)">
    <li><svg viewBox="0 0 18 18" fill="none" stroke="#f7931e" stroke-width="3"><path d="M2 9l5 5 9-11"/></svg>Repair or install a device today.</li>
    <li><svg viewBox="0 0 18 18" fill="none" stroke="#f7931e" stroke-width="3"><path d="M2 9l5 5 9-11"/></svg>Guaranteed parts and service + 24/7 support</li>
    <li><svg viewBox="0 0 18 18" fill="none" stroke="#f7931e" stroke-width="3"><path d="M2 9l5 5 9-11"/></svg>Hundreds of repair and install options</li>
  </ul>
  <a class="btn" style="left:111px;top:3100px;width:125px;height:55px">Contact Us</a>
  <div class="mount-photo" role="img" aria-label="Flat-screen TV on an articulating wall mount arm"></div>
</section>

<!-- News -->
<section class="news">
  <h2>Our <b>Latest News</b></h2>
  <p class="lead">Nemo enim ipsam voluptatem quia voluptas sit aspernatur aut odit aut fugit, sed quia consequuntur magni dolores eos qui ratione voluptatem sequi nesciunt.</p>
  <article class="post" style="left:111px">
    <div class="img" role="img" aria-label="Technician installing a security camera with a homeowner" style="background:linear-gradient(135deg,#3d5580,#c8b6a4)"></div>
    <h3>NEMO ENIM VOLUPTATEM<br>QUIA VOLUPTAS</h3>
    <p>Sed ut perspiciatis unde omnis iste natus error sit voluptatem accusantium dolor emque laudantium.</p>
    <span class="more">READ MORE</span>
  </article>
  <article class="post hot" style="left:447px">
    <div class="img" role="img" aria-label="Hands holding a phone with smart home controls" style="background:linear-gradient(135deg,#d9d4cf,#6f7f96)"></div>
    <h3>NEMO ENIM VOLUPTATEM<br>QUIA VOLUPTAS</h3>
    <p>Sed ut perspiciatis unde omnis iste natus error sit voluptatem accusantium dolor emque laudantium.</p>
    <span class="more">READ MORE</span>
  </article>
  <article class="post" style="left:781px">
    <div class="img" role="img" aria-label="Technician repairing an open smartphone circuit board" style="background:linear-gradient(135deg,#2f3d55,#8aa0b8)"></div>
    <h3>NEMO ENIM VOLUPTATEM<br>QUIA VOLUPTAS</h3>
    <p>Sed ut perspiciatis unde omnis iste natus error sit voluptatem accusantium dolor emque laudantium.</p>
    <span class="more">READ MORE</span>
  </article>
</section>

<!-- Footer -->
<footer class="footer">
  <div class="mark">Brava Nest</div>
  <div class="fcol" style="left:471px"><h5>COMPANY</h5><a>Home</a><a>About Us</a><a>Services</a><a>Solution</a><a>Features</a><a>Blog</a></div>
  <div class="fcol" style="left:642px"><h5>RESOURCES</h5><a>Locations</a><a>Support</a><a>Office Locations</a><a>Contact Us</a></div>
  <div class="fcol" style="left:849px"><h5>CONTACT US</h5>
    <div class="contact-item"><span class="ic"><svg width="18" height="18" viewBox="0 0 18 18" fill="none" stroke="#fff" stroke-width="1.6"><path d="M9 17s6-6 6-10A6 6 0 0 0 3 7c0 4 6 10 6 10z"/><circle cx="9" cy="7" r="2"/></svg></span><span>48 Harlow Lane<br>Austin 73301 TX</span></div>
    <div class="contact-item"><span class="ic"><svg width="18" height="18" viewBox="0 0 18 18" fill="none" stroke="#fff" stroke-width="1.6"><path d="M4 2l3 3-2 2c1 2 3 4 5 5l2-2 3 3-2 2C8 15 3 10 2 4z"/></svg></span><span style="padding-top:4px">+1800 0000 12</span></div>
    <div class="contact-item"><span class="ic"><svg width="18" height="18" viewBox="0 0 18 18" fill="none" stroke="#fff" stroke-width="1.6"><rect x="2" y="4" width="14" height="10"/><path d="M2 4l7 6 7-6"/></svg></span><span style="padding-top:4px">hello@bravanest.example</span></div>
  </div>
  <div class="rule"></div>
  <div class="copy">Copyrights @ 2020 BravaNest. All Rights Reserved.</div>
</footer>

</body>
</html>
```